Card Design Project

A simple, funky, cool birth announcement card
Not corporate, but arty
Not childish nor girlish
No baby pictures

Text is tbc (eg name and date may change)

Front side: just the name "roos"
Should be easy to read

Back side text (in Dutch):

We vinden je nu al leuk!

20 JUNE 2013
Singapore

Dochter van Marieke Vos & Geert Bakker

Yangon, Myanmar
+95 1 48 7361
Skype: Marieke.Vos
Skype: Geert.Bakker

Size will be A6
Updates

Reason: Dear designers, At this stage we would like to have one or more designers to draft up the card (of which the final text is still tbd as the baby is yet to be born) using the typeface used on the left below (or similar!) of the newly added picture - in black - in fluorescent colours Can you get back to us in a few days? Thanks

Target Market(s)

Our funky friends in holland.

Industry/Entity Type

Baby

Requirements
Must have
• Colours, aswe are very happy to welcome this baby.
Something that makes it stand out from all other baby birth announcement cards

A6 size
Deadline 21 June
Printing will be on white (thick paper 250g)
Design for 5mm "bleedsides" all around
At least available in PDF (and other formats)
Nice to have
• We've recently moved from netherlands to Yangon
We could include the iconic thirikyaw pagoda

I would like for it to look like a cool party announcement

Include bright fluoriscent colours, including orange.
The enveloppe will be orange
Should not have
• Any baby stuff, soft pink dominance, childish stuff.

```html
<!DOCTYPE html>
<html lang="nl">
<head>
<meta charset="utf-8">
<title>Roos – geboortekaart voorkant</title>
<link rel="stylesheet" href="https://fonts.googleapis.com/css2?family=Bowlby+One&display=swap">
<style>
  :root {
    --ink-dark: #2a1c10;
    --orange-deep: #d8391a;
    --orange: #ee6a26;
    --orange-light: #f3a45a;
    --sand: #f3d3a0;
    --green: #5f8a2c;
    --green-dark: #2f3f18;
    --cream: #fffaf0;
    --cream-shade: #f6e7c9;
    --outline: #e0501c;
  }
  html, body {
    margin: 0;
    padding: 0;
    width: 1200px;
    height: 866px;
    overflow: hidden;
    background: var(--ink-dark);
  }
  .card-front {
    position: relative;
    width: 1200px;
    height: 866px;
    overflow: hidden;
  }
  .painted-backdrop {
    position: absolute;
    inset: 0;
    background:
      radial-gradient(ellipse 260px 360px at 700px 420px, var(--sand) 0%, rgba(243,211,160,0) 100%),
      radial-gradient(ellipse 300px 260px at 260px 330px, var(--orange-light) 0%, rgba(243,164,90,0) 100%),
      radial-gradient(ellipse 420px 220px at 420px 720px, var(--orange-deep) 0%, rgba(216,57,26,0) 100%),
      radial-gradient(ellipse 380px 220px at 900px 740px, var(--orange) 0%, rgba(238,106,38,0) 100%),
      radial-gradient(ellipse 260px 420px at 1080px 260px, var(--green) 0%, rgba(95,138,44,0) 100%),
      radial-gradient(ellipse 200px 360px at 40px 620px, var(--green) 0%, rgba(95,138,44,0) 100%),
      radial-gradient(ellipse 520px 440px at 560px 430px, var(--orange) 0%, rgba(238,106,38,0) 100%),
      linear-gradient(160deg, var(--green-dark) 0%, var(--orange-deep) 45%, var(--orange) 65%, var(--green-dark) 100%);
  }
  .baby-name {
    position: absolute;
    left: 0;
    right: 0;
    top: 290px;
    margin: 0;
    text-align: center;
    font-family: "Bowlby One", "Arial Black", sans-serif;
    font-weight: 400;
    font-size: 262px;
    line-height: 1;
    letter-spacing: 2px;
    text-transform: uppercase;
    padding-left: 20px;
    color: var(--cream);
    background: linear-gradient(180deg, var(--cream) 30%, var(--cream-shade) 100%);
    -webkit-background-clip: text;
    background-clip: text;
    -webkit-text-fill-color: transparent;
    -webkit-text-stroke: 3px var(--outline);
    filter: drop-shadow(0 0 6px rgba(255, 240, 210, 0.6));
    transform: rotate(-4deg);
  }
</style>
</head>
<body>
  <main class="card-front">
    <div class="painted-backdrop" role="img" aria-label="Abstract painted background of overlapping orange, red, cream and green blotches and squares"></div>
    <h1 class="baby-name">roos</h1>
  </main>
</body>
</html>
```